We require a business card that promotes our Electrical business. Things we would like included are;
1) our business name, Bright Path Electrical and Communication
2) Our Electrical licence, EC 27036
3) Our ABN, 52 147 906 318
4) Our website, www.ridgewirecrew.com.au
5) Our Email, info@ridgewirecrew.com.au
6) Our contact number, 0452 681 207
7) Our address, 48 Marlow Rd Tandridge Perth 6093
8) Our logo, I will attach this (can you please change it so the ackground is white not black)
9) Our colours are red and white and perhaps some black
10) Managing Director Dorian Velcourt
11) the back to say 'notes' and have some lines for writing

Target Market(s)

General

Industry/Entity Type

Electrical

Contact Information for Business Card

Include the colour white, black and red.

Font styles to use
Sans Serif

Requirements
Nice to have
• A thunder bolt or a power point or a cord or something electrical, cartoon image of a cartoon like electrical tradie

```html
<!DOCTYPE html>
<html lang="en">
<head>
<meta charset="utf-8">
<title>Bright Path Electrical and Communication – Business Card</title>
<link rel="stylesheet" href="https://fonts.googleapis.com/css2?family=Lato:wght@400;700;900&display=swap">
<style>
  :root {
    --red: #e3202a;
    --ink: #111111;
    --paper: #ffffff;
    --backdrop: #ececec;
    --rule: #1a1a1a;
  }
  * { box-sizing: border-box; margin: 0; padding: 0; }
  html, body {
    width: 1200px;
    height: 863px;
    overflow: hidden;
    background: var(--backdrop);
    font-family: "Lato", Arial, sans-serif;
    color: var(--ink);
  }
  .sheet {
    position: relative;
    width: 1200px;
    height: 863px;
    display: flex;
    justify-content: center;
    align-items: center;
    gap: 80px;
  }
  .card {
    position: relative;
    width: 340px;
    height: 556px;
    background: var(--paper);
    box-shadow: 0 6px 20px rgba(0,0,0,0.12);
    overflow: hidden;
  }

  /* Back: notes */
  .notes-title {
    margin-top: 34px;
    text-align: center;
    font-weight: 900;
    font-size: 34px;
    letter-spacing: 1px;
    color: var(--ink);
  }
  .notes-lines {
    list-style: none;
    margin: 14px 0 0;
  }
  .notes-lines li {
    height: 47px;
    border-top: 2px solid var(--rule);
  }

  /* Front: contact */
  .corner {
    position: absolute;
    width: 58px;
    height: 58px;
  }
  .corner--top { top: 0; right: 0; }
  .corner--bottom { bottom: 0; left: 0; }
  .corner polygon { fill: var(--red); }

  .front-content {
    position: absolute;
    inset: 0;
    display: flex;
    flex-direction: column;
    align-items: center;
    text-align: center;
    padding-top: 70px;
  }
  .brand-dot {
    width: 64px;
    height: 64px;
    border-radius: 50%;
    background: var(--red);
  }
  .brand-name {
    margin-top: 16px;
    font-weight: 900;
    font-size: 21px;
    line-height: 1.2;
    color: var(--ink);
    max-width: 260px;
  }
  .person-name {
    margin-top: 20px;
    font-weight: 900;
    font-size: 20px;
    color: var(--red);
  }
  .person-role {
    font-size: 16px;
    margin-top: 2px;
  }
  .details {
    font-size: 13px;
    line-height: 1.4;
    margin-top: 22px;
  }
  .details + .details { margin-top: 16px; }
</style>
</head>
<body>
<main class="sheet">
  <section class="card card--back" aria-label="Card back: notes">
    <h2 class="notes-title">NOTES</h2>
    <ul class="notes-lines">
      <li></li><li></li><li></li><li></li><li></li>
      <li></li><li></li><li></li><li></li><li></li>
    </ul>
  </section>

  <section class="card card--front" aria-label="Card front: contact details">
    <svg class="corner corner--top" viewBox="0 0 58 58" aria-hidden="true"><polygon points="0,0 58,0 58,58"/></svg>
    <svg class="corner corner--bottom" viewBox="0 0 58 58" aria-hidden="true"><polygon points="0,0 0,58 58,58"/></svg>
    <div class="front-content">
      <div class="brand-dot" aria-hidden="true"></div>
      <h1 class="brand-name">Bright Path Electrical and Communication</h1>
      <p class="person-name">Dorian Velcourt</p>
      <p class="person-role">Managing Director</p>
      <p class="details">Electrical licence, EC 27036<br>ABN, 52 147 906 318</p>
      <p class="details">0452 681 207<br>www.ridgewirecrew.com.au<br>info@ridgewirecrew.com.au</p>
      <p class="details">48 Marlow Rd<br>Tandridge Perth 6093</p>
    </div>
  </section>
</main>
</body>
</html>
```